Bright Meridian Partners boutique mgt consulting group 5 page web design

I need a 4 - 5 page website that professionally presents the business and what we do/ offer to potential clients. We are a boutique based consultancy business that is cutting edge, focuses on revenue and profit acceleration for our customers primarily focused on (but looking to expand outside of ) the consumer goods and property/ building markets. We are passionate about seeing our clients grow their business and our Experts are not traditional consultants, rather are senior executive experts that specialise in sales, marketing, leadership, coaching, supply chain functions at C suite and below.

I have just had a new logo created and so would like to replicate this feel through the website please.

The final Website design needs to communicate a new era of consulting and freelance experts where technology will support our offer.. it needs to be be on trend, animated, modern, professional and primarily researched by clients on their mobile devices. Whilst a consultancy I don't want our clients to feel it looks the same as a traditional consultancy...

Videos will be added later.

For basic content feel please see existing www.brightmeridianpartners.example website.
I would expect a landing page, our services, about us/ who we are, clients we work with.

The type of website I like the feel of is:
http://cartlumen.example.com.au

Target Market(s)

Business to Business Manufacturers/ Retailers/ Property

Industry/Entity Type

Management Consulting

Coding

Coded - Design and coding required

Number of Pages Required

5+ page

Font styles to use
Sans Serif

Colors

Designer to choose colors to be used in the design.

Requirements
Must have
• 5 pages including landing page, our services, about us/ who we are, clients we work with.
• Modern, professional look
• demonstrate the services
• ability to add video and content later
• Use the logo
• ability to scroll and look up on mobile devices
Nice to have
• Use my logo as watermark
• Moving images
• I like this website:
• https://trovanix.example
• http://cartlumen.example.com.au
• other websites :
• https://skillharbor.example
Should not have
• The look of a traditional Big 4 consulting firm
• Be fixed and static website

```html
<!DOCTYPE html>
<html lang="en">
<head>
<meta charset="utf-8">
<title>Bright Meridian Partners – Our Services</title>
<link href="https://fonts.googleapis.com/css2?family=Rubik:wght@300;400;500&display=swap" rel="stylesheet">
<style>
:root{
  --brand:#1c5aa0;
  --brand-dark:#1b4f8c;
  --accent:#1a9ad6;
  --ink:#222;
  --muted:#777;
  --nav:#6b5b45;
  --white:#fff;
  --footer:#1f5b9e;
  --footer-line:rgba(255,255,255,.18);
}
*{box-sizing:border-box;margin:0;padding:0}
html,body{width:716px;height:1200px;overflow:hidden}
body{font-family:"Rubik",Arial,sans-serif;color:var(--ink);background:var(--white);position:relative}

.site-header{position:absolute;top:0;left:0;width:716px;height:32px;background:var(--white);display:flex;align-items:center;justify-content:space-between;padding:0 35px 0 32px;z-index:5}
.brand{display:flex;align-items:center;gap:7px;font-size:6.5px;font-weight:500;color:var(--brand);text-transform:uppercase}
.brand-square{width:14px;height:14px;background:var(--brand)}
.main-nav{display:flex;align-items:center;gap:8px;font-size:6px;font-weight:500;color:var(--nav);text-transform:uppercase}
.nav-cta{border:1.3px solid #111;color:#111;padding:3px 10px;letter-spacing:.3px}

.hero{position:absolute;top:32px;left:0;width:716px;height:162px;color:var(--white);text-align:center}
.photo{position:absolute;inset:0}
.hero .photo{background:linear-gradient(100deg,#2f3b44 0%,#1e2326 40%,#2a2c2c 70%,#3a3d3d 100%)}
.hero-content{position:relative;padding-top:25px}
.hero h1{font-weight:300;font-size:17px;margin-bottom:12px}
.hero p{font-size:5.4px;line-height:9.5px;width:355px;margin:0 auto}
.hero .tagline{margin-top:10px}

.intro{position:absolute;top:194px;left:0;width:716px;height:74px;text-align:center}
.intro .rule{position:absolute;left:306px;width:104px;height:1px;background:var(--accent)}
.intro .rule.top{top:17px}.intro .rule.bottom{top:56px}
.intro p{position:absolute;top:32px;width:100%;font-size:8px}

.service{position:absolute;left:0;width:716px;overflow:hidden}
.service-text{position:absolute;top:36px}
.service h2{font-weight:300;font-size:17px;margin-bottom:10px;letter-spacing:.2px}
.service ul{list-style:none;font-size:8.2px;line-height:14.4px}
.service.left .service-text{left:155px;text-align:left}
.service.right .service-text{right:155px;text-align:right}
.strategic{top:268px;height:170px;color:#111}
.strategic .photo{background:linear-gradient(90deg,#9fb0c8 0%,#c9d2e2 35%,#e6e9f0 65%,#cfd6e0 100%)}
.customer{top:438px;height:155px;color:var(--white)}
.customer .photo{background:linear-gradient(90deg,#1a1a1a 0%,#2c2d2e 50%,#4a4b4d 75%,#262627 100%)}
.consumer{top:593px;height:156px;color:var(--white)}
.consumer .photo{background:linear-gradient(90deg,#161616 0%,#1f1f1f 45%,#3b3533 70%,#1c1b1b 100%)}
.supply{top:749px;height:170px;color:var(--white)}
.supply .photo{background:linear-gradient(90deg,#b8b2b4 0%,#c9c1c4 35%,#c3b8bd 100%)}
.service-text{z-index:1}
.scroll-arrow{position:absolute;left:662px;top:128px}

.stats{position:absolute;top:919px;left:0;width:716px;height:157px}
.stat{position:absolute;top:56px;width:112px;text-align:center;transform:translateX(-50%)}
.stat strong{display:block;font-weight:300;font-size:18px;margin-bottom:6px}
.stat p{font-size:5.4px;line-height:9px;color:var(--muted)}
.to-top{position:absolute;left:659px;top:99px;width:23px;height:23px;background:#ddd;display:flex;align-items:center;justify-content:center}

.site-footer{position:absolute;top:1076px;left:0;width:716px;height:124px;background:var(--footer);color:var(--white)}
.footer-brand{position:absolute;left:155px;top:39px;font-size:4.5px;font-weight:500;text-transform:uppercase;display:flex;align-items:center;gap:3px}
.footer-brand span.sq{width:8px;height:8px;background:var(--white)}
.footer-col{position:absolute;top:24px}
.footer-col h3{font-size:7px;font-weight:500;margin-bottom:9px}
.footer-col p{font-size:5.5px;line-height:9.5px}
.footer-rule{position:absolute;left:155px;top:78px;width:406px;height:1px;background:var(--footer-line)}
.copyright{position:absolute;left:155px;top:87px;font-size:5.5px}
.social{position:absolute;left:522px;top:87px;display:flex;gap:6px}
.social span{width:7px;height:7px;border-radius:50%;background:rgba(255,255,255,.75)}
</style>
</head>
<body>

<header class="site-header">
  <div class="brand"><span class="brand-square"></span>Bright Meridian Partners</div>
  <nav class="main-nav">
    <span>Home</span><span>Services</span><span>Who We Are</span><span>Our Clients</span>
    <span class="nav-cta">Contact Us</span>
  </nav>
</header>

<section class="hero">
  <div class="photo" role="img" aria-label="Dimmed photo of a desk with laptop, charts and glasses"></div>
  <div class="hero-content">
    <h1>Our Services</h1>
    <p>Whether you have the need to unlock the strategic vision to keep pace in the market, improve your customer and consumer relevance, help make the business move faster at an operational level, simplify the processes to get focus, refine the way you go to market, sell, negotiate and create high performing teams.....</p>
    <p class="tagline">Bright Meridian Partners will help you win</p>
  </div>
</section>

<section class="intro">
  <span class="rule top"></span>
  <p>We are proven experts in the Consumer Products and Services Marketplace</p>
  <span class="rule bottom"></span>
</section>

<section class="service left strategic">
  <div class="photo" role="img" aria-label="Photo of a hand pointing at charts on a glass wall"></div>
  <div class="service-text">
    <h2>Strategic Focus</h2>
    <ul><li>Strategic Joined Up Business Planning</li><li>Coaching C Suite &amp; Below</li><li>Creating High Performing Teams</li><li>Facilitating Workshops</li></ul>
  </div>
</section>

<section class="service right customer">
  <div class="photo" role="img" aria-label="Dark photo of a business handshake across a desk"></div>
  <div class="service-text">
    <h2>Customer Focus</h2>
    <ul><li>Unlocking Strategic Customer Partnerships</li><li>Selling and Negotiation</li><li>Trading Terms Strategies &amp; Investment</li></ul>
  </div>
</section>

<section class="service left consumer">
  <div class="photo" role="img" aria-label="Dark photo of a smiling shopper"></div>
  <div class="service-text">
    <h2>Consumer Focus</h2>
    <ul><li>Consumer Pricing Strategies</li><li>Consumer Insights</li><li>Category Management</li></ul>
  </div>
  <svg class="scroll-arrow" width="14" height="14" viewBox="0 0 14 14" aria-hidden="true"><path d="M7 13V1M1 7l6-6 6 6" fill="none" stroke="#fff" stroke-width="1"/></svg>
</section>

<section class="service right supply">
  <div class="photo" role="img" aria-label="Soft photo of a potted plant beside a desk lamp and monitor"></div>
  <div class="service-text">
    <h2>Supply Chain Focus</h2>
    <ul><li>Procurement Joined up Planning</li><li>Integrated S&amp;OP processes</li><li>Route to Consumer Strategies</li><li>Supply Chain Improvement</li></ul>
  </div>
</section>

<section class="stats">
  <div class="stat" style="left:222px"><strong>100</strong><p>SOME of our Clients come to us to help embed leadership or unlock their Strategic Vision to keep pace in an ever changing marketplace</p></div>
  <div class="stat" style="left:358px"><strong>200</strong><p>MOST of our clients come to us to implement global best practice planning, systems and processes with the teams to accelerate performance.</p></div>
  <div class="stat" style="left:494px"><strong>300</strong><p>ALL of our clients want us to help to coach and build high performing teams and talent capability to future proof their success</p></div>
  <div class="to-top"><svg width="12" height="12" viewBox="0 0 12 12" aria-hidden="true"><path d="M6 11V1M1.5 5.5 6 1l4.5 4.5" fill="none" stroke="#fff" stroke-width="1"/></svg></div>
</section>

<footer class="site-footer">
  <div class="footer-brand"><span class="sq"></span>Bright Meridian Partners</div>
  <div class="footer-col" style="left:259px"><h3>Address</h3><p>Harbour Vale<br>NSW 2999</p></div>
  <div class="footer-col" style="left:363px"><h3>Contacts</h3><p>Email: hello@brightmeridian.example<br>Phone: 0400 000 123</p></div>
  <div class="footer-col" style="left:468px"><h3>Links</h3><p>Services<br>About<br>Clients</p></div>
  <div class="footer-rule"></div>
  <p class="copyright">© Copyright 2017 Bright Meridian - All Rights Reserved</p>
  <div class="social" aria-label="Social links"><span></span><span></span><span></span></div>
</footer>

</body>
</html>
```